Redesign website for small print company

Vindaborgprent is a small printing company in Iceland mainly servicing Students, schools, etc. We are also doing all kind of other jobs, like business cards, book printing, brochure printing etc. We are also selling books online.
Our website is: www.vindaborgprent.is
What we are looking for is:
- Web Design (Uncoded - PSD layout only)
- Mobile friendly design, using our current color scheme: Red, green, yellow and light gray.
- Clean simple design
- Simple, light and easy to use.
- More menu Items/drop down
Industry/Entity Type
Digital Printing
Number of Pages Required
5+ page
Requirements
Must have
- Easy navigation
- Designed for mobile
- Current color scheme (see logo)
Nice to have
- Icon based products

```html
<!DOCTYPE html>
<html lang="en">
<head>
<meta charset="utf-8">
<title>Vindaborgprent – Small Printing Company in Iceland</title>
<link href="https://fonts.googleapis.com/css2?family=Lato:wght@400;700;900&family=Open+Sans:wght@400;600;700&display=swap" rel="stylesheet">
<style>
:root{
  --red:#c8202a;
  --green:#5cb85c;
  --dark:#222222;
  --footer:#1e1e1e;
  --text:#333333;
  --muted:#7a7a7a;
  --light:#f3f3f3;
  --line:#e3e3e3;
  --white:#ffffff;
}
*{box-sizing:border-box;margin:0;padding:0}
html,body{width:1200px;height:4018px;overflow:hidden}
body{font-family:"Open Sans",Arial,sans-serif;color:var(--text);background:var(--white);position:relative}
h1,h2,h3,h4{font-family:"Lato",Arial,sans-serif}
.btn{display:inline-block;font-family:"Open Sans",Arial,sans-serif;font-size:12px;font-weight:600;text-transform:uppercase;color:var(--white);background:var(--red);padding:0 22px;line-height:38px}
.btn-dark{background:var(--dark)}

/* top bar */
.topbar{position:absolute;left:0;top:0;width:1200px;height:27px;background:var(--dark);color:var(--white);font-size:12px}
.topbar .mail{position:absolute;left:838px;top:4px;height:19px;padding:0 10px 0 26px;line-height:19px;background:var(--red);border-radius:2px}
.topbar .mail svg{position:absolute;left:8px;top:5px}
.topbar .phone{position:absolute;left:1060px;top:4px;line-height:19px;padding-left:18px}
.topbar .phone svg{position:absolute;left:0;top:4px}

/* header */
.header{position:absolute;left:0;top:27px;width:1200px;height:128px;background:var(--white)}
.brand{position:absolute;left:64px;top:48px;font-family:"Lato",Arial,sans-serif;font-weight:700;font-size:28px;color:var(--dark);white-space:nowrap}
.nav{position:absolute;left:448px;top:59px;display:flex;gap:24px;font-size:13.5px;color:var(--dark);text-transform:uppercase}
.quote-btn{position:absolute;left:998px;top:46px;width:150px;height:42px;border-radius:21px;background:var(--green);color:var(--white);font-weight:700;font-size:13px;text-align:center;line-height:42px}

/* hero */
.hero{position:absolute;left:0;top:155px;width:1200px;height:359px;background:linear-gradient(90deg,#f4f4f4 0%,#ececec 45%,#e2e2e2 100%)}
.hero-photo{position:absolute;left:560px;top:0;width:640px;height:359px;background:linear-gradient(120deg,#d9d4cd 0%,#b9a792 40%,#8d7b6c 70%,#c9c0b6 100%)}
.hero-fade{position:absolute;left:560px;top:0;width:200px;height:359px;background:linear-gradient(90deg,#ececec 0%,rgba(236,236,236,0) 100%)}
.hero h1{position:absolute;left:76px;top:62px;font-size:40px;font-weight:400;line-height:48px;color:var(--dark)}
.hero h1 em{font-style:normal;color:var(--red)}
.hero p{position:absolute;left:80px;top:172px;width:380px;font-size:13.5px;line-height:22px;color:var(--text)}
.hero .actions{position:absolute;left:80px;top:265px;display:flex;gap:14px}

/* partners */
.partners{position:absolute;left:0;top:514px;width:1200px;height:124px;border-bottom:1px solid var(--line);display:flex;justify-content:center;align-items:center;gap:48px}
.partners span{display:block;width:128px;height:32px;background:#e6e6e6;border-radius:3px}

/* intro */
.intro{position:absolute;left:0;top:690px;width:1200px;text-align:center}
.intro h2{font-size:32px;font-weight:400;line-height:42px;color:var(--dark)}
.intro h2 em{font-style:normal;color:var(--red)}
.intro p{margin:26px auto 0;width:780px;font-size:13.5px;line-height:24px;color:var(--muted)}

/* service cards */
.service{position:absolute;width:340px;height:268px;border:1px solid var(--line);background:var(--white);text-align:center}
.service.lift{box-shadow:0 14px 26px rgba(0,0,0,.13);border-color:#eee}
.service svg{margin-top:30px}
.service h3{margin-top:10px;font-size:19px;font-weight:700;color:var(--dark)}
.service p{margin:10px auto 0;width:250px;font-size:13px;line-height:19px;color:var(--muted)}
.service .btn{margin-top:16px;font-size:11px;line-height:30px;padding:0 14px}

/* strategy */
.strategy{position:absolute;left:0;top:1640px;width:1200px;height:460px;background:var(--light)}
.strategy h2{position:absolute;left:128px;top:64px;font-size:36px;font-weight:400;color:var(--dark)}
.strategy p{position:absolute;left:132px;top:130px;width:460px;font-size:13px;line-height:22px;color:var(--text)}
.checks{position:absolute;display:grid;grid-template-columns:270px 200px;row-gap:16px;font-size:12.5px;font-weight:700;color:var(--dark);text-transform:uppercase}
.checks li{list-style:none;display:flex;align-items:center;gap:12px}
.strategy .btn{position:absolute;left:136px;top:378px;font-size:11px;line-height:34px;padding:0 18px}
.strategy-photo{position:absolute;left:662px;top:85px;width:446px;height:271px;background:linear-gradient(135deg,#d8dbe0 0%,#b7bcc4 45%,#8c919a 100%)}
.play{position:absolute;left:846px;top:191px}

/* projects */
.projects{position:absolute;left:0;top:2100px;width:1200px;height:726px}
.projects h2{position:absolute;left:0;top:66px;width:1200px;text-align:center;font-size:28px;font-weight:700;line-height:40px;color:var(--dark)}
.projects h2 span{font-weight:400}
.projects h2 em{font-style:normal;color:var(--red);font-weight:700}
.projects .lead{position:absolute;left:270px;top:180px;width:660px;text-align:center;font-size:13px;line-height:22px;color:var(--muted)}
.project{position:absolute;top:290px;width:250px;height:302px;background:#f6f6f6;text-align:center}
.project .shot{height:150px}
.project h4{margin-top:26px;font-family:"Open Sans",Arial,sans-serif;font-size:12.5px;font-weight:700;color:var(--red);text-transform:uppercase}
.project p{margin:12px auto 0;width:200px;font-size:12px;line-height:18px;color:var(--muted)}
.project .links{margin-top:14px;display:flex;justify-content:space-around;font-size:11px;color:var(--red)}
.projects .btn{position:absolute;left:499px;top:632px;width:202px;text-align:center;font-size:12px;line-height:36px}

/* quote */
.quote{position:absolute;left:0;top:2826px;width:1200px;height:684px;background:var(--light)}
.quote h2{position:absolute;left:128px;top:108px;font-size:30px;font-weight:700;line-height:40px;color:var(--dark)}
.quote h2 em{font-style:normal;color:var(--red)}
.quote p{position:absolute;left:132px;top:222px;width:450px;font-size:13px;line-height:22px;color:var(--text)}
.quote .btn{position:absolute;left:136px;top:510px;font-size:11px;line-height:34px;padding:0 18px}
.form{position:absolute;left:729px;top:76px;width:356px;height:584px;background:var(--white);box-shadow:0 6px 22px rgba(0,0,0,.09);padding:40px 44px 0 44px}
.form label{display:block;font-size:10.5px;font-weight:700;color:var(--dark);text-transform:uppercase;letter-spacing:.3px;line-height:15px}
.form label b{color:var(--red);margin-left:4px}
.form .field{height:38px;border:1px solid var(--line);margin:10px 0 24px}
.form .area{height:104px;border:1px solid var(--line);margin:10px 0 14px}
.form .submit{height:38px;background:var(--green);color:var(--white);text-align:center;line-height:38px;font-size:13.5px;font-weight:600;text-transform:uppercase}

/* footer */
.footer{position:absolute;left:0;top:3510px;width:1200px;height:508px;background:var(--footer);color:#cfcfcf}
.footer h4{font-size:18px;font-weight:700;color:var(--white)}
.fcol{position:absolute;top:82px}
.fcol ul{list-style:none;margin-top:20px}
.fcol li{font-size:12.5px;line-height:33px;color:#bdbdbd}
.contact li{position:relative;padding-left:30px;line-height:22px;margin-bottom:18px}
.contact svg{position:absolute;left:0;top:4px}
.quick h4{display:inline-block;background:#2c2c2c;padding:6px 12px}
.newsletter .note{margin-top:18px;font-size:12.5px;color:#bdbdbd}
.subscribe{margin-top:12px;display:flex;width:336px;height:40px}
.subscribe .in{flex:1;background:#3a3a3a;color:#9a9a9a;font-size:12px;line-height:40px;padding-left:34px;position:relative}
.subscribe .in svg{position:absolute;left:10px;top:13px}
.subscribe .go{width:96px;background:var(--green);color:var(--white);font-size:12px;font-weight:700;text-align:center;line-height:40px;text-transform:uppercase}
.newsletter h5{margin-top:40px;font-family:"Lato",Arial,sans-serif;font-size:18px;color:var(--white)}
.social{margin-top:20px;display:flex;gap:14px}
.social span{width:34px;height:34px;border-radius:50%}
.footer .rule{position:absolute;left:58px;top:410px;width:1084px;height:1px;background:#333}
.footer .copy{position:absolute;left:0;top:448px;width:1200px;text-align:center;font-size:12px;color:#9a9a9a}
</style>
</head>
<body>

<div class="topbar">
  <div class="mail"><svg width="12" height="9" viewBox="0 0 12 9"><rect x=".5" y=".5" width="11" height="8" fill="none" stroke="#fff"/><path d="M.5 .5 6 5l5.5-4.5" fill="none" stroke="#fff"/></svg>verk@vindaborgprent.is</div>
  <div class="phone"><svg width="11" height="11" viewBox="0 0 24 24"><path fill="#c8202a" d="M6.6 10.8c1.4 2.8 3.8 5.1 6.6 6.6l2.2-2.2c.3-.3.7-.4 1-.2 1.1.4 2.3.6 3.6.6.6 0 1 .4 1 1V20c0 .6-.4 1-1 1C10.6 21 3 13.4 3 4c0-.6.4-1 1-1h3.5c.6 0 1 .4 1 1 0 1.3.2 2.5.6 3.6.1.3 0 .7-.2 1z"/></svg>Tel: 555 0142</div>
</div>

<header class="header">
  <div class="brand">Vindaborgprent</div>
  <nav class="nav"><span>Home</span><span>About us</span><span>Services</span><span>Prices</span><span>Portfolio</span><span>Method</span><span>Contact</span></nav>
  <div class="quote-btn">GET QUOTE</div>
</header>

<section class="hero">
  <div class="hero-photo" role="img" aria-label="Photo of a group of young students gathered around a laptop in a bright room"></div>
  <div class="hero-fade"></div>
  <h1>We Are&nbsp; Small Printing Company<br>in <em>Iceland</em></h1>
  <p>We work with a small <b>team of 5 people</b> in the Netherlands and with a <b>large group of freelancers</b> who are all good at their own expertise</p>
  <div class="actions"><span class="btn">Sign up</span><span class="btn btn-dark">Learn more</span></div>
</section>

<section class="partners" aria-label="Partners">
  <span></span><span></span><span></span><span></span><span></span><span></span>
</section>

<section class="intro">
  <h2>Vindaborgprent is a small printing company in<br><em>Iceland</em> mainly servicing <em>Students, schools, etc.</em></h2>
  <p>We are also doing all kind of other jobs, like business cards, book printing, brochure printing etc. We are also selling books online. Vindaborgprent is a Heron certified printing company. The Heron is the official ecolabel of the Nordic countries, which has created a foothold in this country and is known among consumers.</p>
</section>

<div class="service" style="left:54px;top:943px">
  <svg width="44" height="44" viewBox="0 0 44 44" fill="none" stroke="#c8202a" stroke-width="2"><rect x="10" y="6" width="24" height="32"/><path d="M15 14h14M15 20h14M15 26h9"/><path d="M30 30l6-6 3 3-6 6h-3z"/></svg>
  <h3>Essays</h3>
  <p>All websites are made in consultation with the customer. The customer has full input into the appearance</p>
  <span class="btn">Learn more</span>
</div>
<div class="service lift" style="left:431px;top:943px">
  <svg width="44" height="44" viewBox="0 0 44 44" fill="none" stroke="#c8202a" stroke-width="2"><rect x="6" y="12" width="32" height="22" rx="2"/><circle cx="15" cy="21" r="3"/><path d="M10 29c1-3 9-3 10 0M24 19h10M24 24h10M24 29h6"/><rect x="18" y="7" width="8" height="6"/></svg>
  <h3>Business cards</h3>
  <p>All websites are made in consultation with the customer. The customer has full input into the appearance</p>
  <span class="btn">Learn more</span>
</div>
<div class="service" style="left:798px;top:943px">
  <svg width="44" height="44" viewBox="0 0 44 44" fill="none" stroke="#c8202a" stroke-width="2"><rect x="13" y="5" width="18" height="34" rx="2"/><path d="M18 12h8M18 18h8M18 24h5"/><circle cx="22" cy="33" r="1.5"/></svg>
  <h3>Leafleats</h3>
  <p>All websites are made in consultation with the customer. The customer has full input into the appearance</p>
  <span class="btn">Learn more</span>
</div>
<div class="service" style="left:54px;top:1286px">
  <svg width="44" height="44" viewBox="0 0 44 44" fill="none" stroke="#c8202a" stroke-width="2"><rect x="12" y="6" width="20" height="10"/><rect x="6" y="16" width="32" height="14" rx="2"/><rect x="12" y="26" width="20" height="12"/><path d="M16 31h12M16 35h8"/></svg>
  <h3>Bookprinting</h3>
  <p>All websites are made in consultation with the customer. The customer has full input into the appearance</p>
  <span class="btn">Learn more</span>
</div>
<div class="service" style="left:431px;top:1286px">
  <svg width="44" height="44" viewBox="0 0 44 44" fill="none" stroke="#c8202a" stroke-width="2"><rect x="11" y="8" width="22" height="30" rx="2"/><path d="M18 5h8v6h-8z"/><circle cx="22" cy="24" r="6"/><path d="M22 21v3l2 2"/></svg>
  <h3>Posters</h3>
  <p>All websites are made in consultation with the customer. The customer has full input into the appearance</p>
  <span class="btn">Learn more</span>
</div>
<div class="service" style="left:798px;top:1286px">
  <svg width="44" height="44" viewBox="0 0 44 44" fill="none" stroke="#c8202a" stroke-width="2"><rect x="10" y="5" width="24" height="34"/><path d="M15 12h14M15 17h14M15 22h14M15 27h14M15 32h9"/></svg>
  <h3>Textbooks</h3>
  <p>All websites are made in consultation with the customer. The customer has full input into the appearance</p>
  <span class="btn">Learn more</span>
</div>

<section class="strategy">
  <h2>Our <b>Strategy</b></h2>
  <p>Our mission is to services all small clients from 2 till 50 employes within online marketing and focus on online strategy. brightleafweb.com is a full service internet agency that has been active since 2010. From simple website to complete marketplace like sites we have already made.</p>
  <ul class="checks" style="left:132px;top:245px">
    <li><svg width="20" height="20" viewBox="0 0 20 20"><circle cx="10" cy="10" r="8.5" fill="none" stroke="#c8202a" stroke-width="1.6"/><path d="M6 10.3l2.8 2.7L14 7.5" fill="none" stroke="#c8202a" stroke-width="1.8"/></svg>CMS Website</li>
    <li><svg width="20" height="20" viewBox="0 0 20 20"><circle cx="10" cy="10" r="8.5" fill="none" stroke="#c8202a" stroke-width="1.6"/><path d="M6 10.3l2.8 2.7L14 7.5" fill="none" stroke="#c8202a" stroke-width="1.8"/></svg>Clean code</li>
    <li><svg width="20" height="20" viewBox="0 0 20 20"><circle cx="10" cy="10" r="8.5" fill="none" stroke="#c8202a" stroke-width="1.6"/><path d="M6 10.3l2.8 2.7L14 7.5" fill="none" stroke="#c8202a" stroke-width="1.8"/></svg>Minimum 90 speed score</li>
    <li><svg width="20" height="20" viewBox="0 0 20 20"><circle cx="10" cy="10" r="8.5" fill="none" stroke="#c8202a" stroke-width="1.6"/><path d="M6 10.3l2.8 2.7L14 7.5" fill="none" stroke="#c8202a" stroke-width="1.8"/></svg>Fast website</li>
    <li><svg width="20" height="20" viewBox="0 0 20 20"><circle cx="10" cy="10" r="8.5" fill="none" stroke="#c8202a" stroke-width="1.6"/><path d="M6 10.3l2.8 2.7L14 7.5" fill="none" stroke="#c8202a" stroke-width="1.8"/></svg>Highest code</li>
    <li><svg width="20" height="20" viewBox="0 0 20 20"><circle cx="10" cy="10" r="8.5" fill="none" stroke="#c8202a" stroke-width="1.6"/><path d="M6 10.3l2.8 2.7L14 7.5" fill="none" stroke="#c8202a" stroke-width="1.8"/></svg>SSL</li>
  </ul>
  <span class="btn">Learn more</span>
  <div class="strategy-photo" role="img" aria-label="Video still of a team working at desks in a bright office"></div>
  <svg class="play" width="56" height="56" viewBox="0 0 56 56"><circle cx="28" cy="28" r="27" fill="#c8202a"/><circle cx="28" cy="28" r="20" fill="none" stroke="#fff" stroke-width="2"/><path d="M23 19l14 9-14 9z" fill="#fff"/></svg>
</section>

<section class="projects">
  <h2>We will never a Client who is not Satisfied with our Project<br><span>All our Projects must be</span> <em>100% satisfied</em></h2>
  <p class="lead">Our mission is to services all small clients from 2 till 50 employes within online marketing and focus on online strategy. brightleafweb.com is a full service internet agency that has been active since 2010 website to complete marketplace like sites we have already made.</p>

  <div class="project" style="left:80px">
    <div class="shot" role="img" aria-label="Photo of stacked printed books" style="background:linear-gradient(135deg,#e9e3d6,#c9a86a 45%,#7a6a5a)"></div>
    <h4>Book printing</h4>
    <p>Our mission is to services all small clients from 2 till 50 employes</p>
    <div class="links"><span>View more →</span><span>View project →</span></div>
  </div>
  <div class="project" style="left:343px">
    <div class="shot" role="img" aria-label="Photo of a printed text book cover" style="background:linear-gradient(135deg,#f2efe9,#d9b94a 40%,#c93a3a)"></div>
    <h4>Text book</h4>
    <p>Our mission is to services all small clients from 2 till 50 employes</p>
    <div class="links"><span>View more →</span><span>View project →</span></div>
  </div>
  <div class="project" style="left:605px">
    <div class="shot" role="img" aria-label="Photo of folded printed leaflets" style="background:linear-gradient(135deg,#eef0f3,#9fb4cc 45%,#5d6f86)"></div>
    <h4>Leaflets</h4>
    <p>Our mission is to services all small clients from 2 till 50 employes</p>
    <div class="links"><span>View more →</span><span>View project →</span></div>
  </div>
  <div class="project" style="left:868px">
    <div class="shot" role="img" aria-label="Photo of a rolled-out printed poster" style="background:linear-gradient(135deg,#f1f1f1,#8a8a8a 45%,#1d1d1d)"></div>
    <h4>Poster</h4>
    <p>Our mission is to services all small clients from 2 till 50 employes</p>
    <div class="links"><span>View more →</span><span>View project →</span></div>
  </div>

  <span class="btn">View all projects</span>
</section>

<section class="quote">
  <h2>Yes, send me without obligation<br>my <em>WEBSITE QUOTE</em></h2>
  <p>brightleafweb.com is a full service internet agency that has been active since 2010. From simple website to complete marketplace like sites we have already made. We work with a small team of 5 people in the Netherlands and with a large group of freelancers who are all good at their own expertise such as PHP, HTML5, CMS BUILDS, ONLINE STORES, SEARCH ENGINE OPTIMIZATION, SEARCH ADVERTISING.</p>
  <ul class="checks" style="left:132px;top:378px">
    <li><svg width="20" height="20" viewBox="0 0 20 20"><circle cx="10" cy="10" r="8.5" fill="none" stroke="#c8202a" stroke-width="1.6"/><path d="M6 10.3l2.8 2.7L14 7.5" fill="none" stroke="#c8202a" stroke-width="1.8"/></svg>CMS Website</li>
    <li><svg width="20" height="20" viewBox="0 0 20 20"><circle cx="10" cy="10" r="8.5" fill="none" stroke="#c8202a" stroke-width="1.6"/><path d="M6 10.3l2.8 2.7L14 7.5" fill="none" stroke="#c8202a" stroke-width="1.8"/></svg>Clean code</li>
    <li><svg width="20" height="20" viewBox="0 0 20 20"><circle cx="10" cy="10" r="8.5" fill="none" stroke="#c8202a" stroke-width="1.6"/><path d="M6 10.3l2.8 2.7L14 7.5" fill="none" stroke="#c8202a" stroke-width="1.8"/></svg>Minimum 90 speed score</li>
    <li><svg width="20" height="20" viewBox="0 0 20 20"><circle cx="10" cy="10" r="8.5" fill="none" stroke="#c8202a" stroke-width="1.6"/><path d="M6 10.3l2.8 2.7L14 7.5" fill="none" stroke="#c8202a" stroke-width="1.8"/></svg>Fast website</li>
    <li><svg width="20" height="20" viewBox="0 0 20 20"><circle cx="10" cy="10" r="8.5" fill="none" stroke="#c8202a" stroke-width="1.6"/><path d="M6 10.3l2.8 2.7L14 7.5" fill="none" stroke="#c8202a" stroke-width="1.8"/></svg>Highest code</li>
    <li><svg width="20" height="20" viewBox="0 0 20 20"><circle cx="10" cy="10" r="8.5" fill="none" stroke="#c8202a" stroke-width="1.6"/><path d="M6 10.3l2.8 2.7L14 7.5" fill="none" stroke="#c8202a" stroke-width="1.8"/></svg>SSL</li>
  </ul>
  <span class="btn">Learn more</span>

  <div class="form">
    <label>First name<b>*</b></label><div class="field"></div>
    <label>Company name<b>*</b></label><div class="field"></div>
    <label>E-mail<b>*</b></label><div class="field"></div>
    <label>Phone<b>*</b></label><div class="field"></div>
    <label>Extra information</label><div class="area"></div>
    <div class="submit">Request quote</div>
  </div>
</section>

<footer class="footer">
  <div class="fcol contact" style="left:58px">
    <h4>Contact Us</h4>
    <ul>
      <li><svg width="14" height="14" viewBox="0 0 24 24"><path fill="#fff" d="M21 3 3 10.5l7.5 3 3 7.5z"/></svg>Harbour road, Linden Street 14,<br>Brookvale, Your Country</li>
      <li><svg width="14" height="14" viewBox="0 0 24 24"><path fill="#fff" d="M6.6 10.8c1.4 2.8 3.8 5.1 6.6 6.6l2.2-2.2c.3-.3.7-.4 1-.2 1.1.4 2.3.6 3.6.6.6 0 1 .4 1 1V20c0 .6-.4 1-1 1C10.6 21 3 13.4 3 4c0-.6.4-1 1-1h3.5c.6 0 1 .4 1 1 0 1.3.2 2.5.6 3.6.1.3 0 .7-.2 1z"/></svg>(305) 555-0199, (305) 555-0177</li>
      <li><svg width="14" height="14" viewBox="0 0 24 24"><rect x="2" y="5" width="20" height="14" fill="none" stroke="#fff" stroke-width="2"/><path d="M2 5l10 8 10-8" fill="none" stroke="#fff" stroke-width="2"/></svg>hello@vindaborgprent.is</li>
      <li><svg width="14" height="14" viewBox="0 0 24 24"><circle cx="12" cy="12" r="9" fill="none" stroke="#fff" stroke-width="2"/><path d="M12 7v5l3 3" fill="none" stroke="#fff" stroke-width="2"/></svg>Monday - Friday: 09:00 -<br>18:00 Saturday, Sunday: Closed</li>
    </ul>
  </div>
  <div class="fcol quick" style="left:326px;top:76px">
    <h4>Quick Link</h4>
    <ul>
      <li>About us</li><li>Services</li><li>Career</li><li>Projects</li><li>Blog</li><li>Contact</li>
    </ul>
  </div>
  <div class="fcol" style="left:527px">
    <h4>Services</h4>
    <ul>
      <li>Customer Support</li><li>Bulk time service</li><li>Business branding</li><li>Money exchange</li><li>Consulting Services</li><li>Strategic Planning</li><li>International</li>
    </ul>
  </div>
  <div class="fcol newsletter" style="left:804px">
    <h4>Newsletter</h4>
    <div class="note">Enter your email &amp; subcribing newsletter</div>
    <div class="subscribe">
      <div class="in"><svg width="14" height="12" viewBox="0 0 14 12"><rect x=".5" y=".5" width="13" height="11" fill="none" stroke="#5cb85c"/><path d="M.5 .5 7 6l6.5-5.5" fill="none" stroke="#5cb85c"/></svg>Email address</div>
      <div class="go">Subscribe</div>
    </div>
    <h5>Contact us on</h5>
    <div class="social">
      <span style="background:#3b5998"></span>
      <span style="background:#4a6fa5"></span>
      <span style="background:#d6443a"></span>
      <span style="background:#c8357a"></span>
      <span style="background:#1da1f2"></span>
    </div>
  </div>
  <div class="rule"></div>
  <div class="copy">2018 all rights reserved</div>
</footer>

</body>
</html>
```